Professional Business Card for Commercial Cleaning Company

We need a business card that represents our commercial janitorial cleaning company and represent several brands for our company so we do not want to highlight the logo too much. We want something that says we are professional.
Notes:No website or address as we have many locations and many websites and companies under our corporate name of "Brightwell Holdings, LLC" . Every time we hand a customer a business card they have contacted us via another brand we own but we don't want to have 21 business cards so we want to not focus on Brightwell Holdings, LLC too much since people will automatically ask "What is Brightwell Holdings, LLC" Example: Noodle Barn and Wrap Dome restaurants are owned by "Zing! Brands" is the corporation name. Same principle here. Except we do not advertise at this time that all of our brands are connected. Hope this helps.
Target Market(s)
Commercial Cleaning
Industry/Entity Type
Janitorial Service
Contact Information for Business Card
Miles Hartwin
Business Development
347-628-9043
sales@brightwellholdingsllc.example
Requirements
Must have
- Logo with contact information, need to be able to easily edit contact info for others in my office.
Nice to have
- Professional Image. Like to see a colorful bold look and a more standard business card look.
Should not have
- Any type of cleaning icons, tools, people or water.

```html
<!DOCTYPE html>
<html lang="en">
<head>
<meta charset="utf-8">
<title>Brightwell Holdings, LLC — Business Card</title>
<link href="https://fonts.googleapis.com/css2?family=Montserrat:wght@700&family=Lato:wght@400;700&display=swap" rel="stylesheet">
<style>
  :root {
    --navy: #1f3c7a;
    --green: #5c9f3c;
    --white: #ffffff;
    --backdrop: #2a2a2e;
  }
  * { box-sizing: border-box; margin: 0; padding: 0; }
  html, body {
    width: 1200px;
    height: 800px;
    overflow: hidden;
    background: var(--backdrop);
  }
  .sheet {
    width: 1200px;
    height: 800px;
    display: flex;
    align-items: center;
    justify-content: center;
    gap: 40px;
  }
  .card {
    position: relative;
    width: 540px;
    height: 309px;
    overflow: hidden;
    box-shadow: 0 10px 30px rgba(0,0,0,.45);
  }
  .card--front {
    background: var(--navy);
    display: flex;
    align-items: center;
    justify-content: center;
  }
  .card--back { background: var(--navy); }
  .card__shape {
    position: absolute;
    inset: 0;
    width: 100%;
    height: 100%;
  }
  .wordmark {
    font-family: "Montserrat", sans-serif;
    font-weight: 700;
    letter-spacing: -0.3px;
    white-space: nowrap;
  }
  .card--front .wordmark {
    color: var(--white);
    font-size: 32px;
  }
  .card--back .wordmark {
    position: absolute;
    left: 56px;
    top: 118px;
    color: var(--navy);
    font-size: 26px;
  }
  .contact {
    position: absolute;
    left: 56px;
    bottom: 30px;
    font-family: "Lato", sans-serif;
    color: var(--navy);
  }
  .contact__name {
    font-weight: 700;
    font-size: 16px;
    line-height: 1.1;
  }
  .contact__role {
    color: var(--green);
    font-size: 13px;
    margin-bottom: 10px;
  }
  .contact__line {
    display: flex;
    align-items: center;
    gap: 8px;
    font-size: 13px;
    line-height: 1.55;
  }
  .contact__icon {
    width: 12px;
    height: 12px;
    flex: none;
  }
</style>
</head>
<body>
  <main class="sheet">
    <section class="card card--front" aria-label="Card front">
      <span class="wordmark">Brightwell Holdings, LLC</span>
    </section>

    <section class="card card--back" aria-label="Card back">
      <svg class="card__shape" viewBox="0 0 540 309" preserveAspectRatio="none" aria-hidden="true">
        <path d="M0,0 H190 C340,-10 470,20 505,95 C530,150 515,230 470,309 H0 Z" fill="var(--white)"/>
        <path d="M140,70 C260,15 420,10 480,80 C515,125 510,200 478,280" fill="none" stroke="var(--green)" stroke-width="4" stroke-linecap="round"/>
      </svg>

      <span class="wordmark">Brightwell Holdings, LLC</span>

      <div class="contact">
        <p class="contact__name">Miles Hartwin</p>
        <p class="contact__role">Business Development</p>
        <p class="contact__line">
          <svg class="contact__icon" viewBox="0 0 12 12" aria-hidden="true"><rect x="2" y="0.75" width="8" height="10.5" rx="1.2" fill="none" stroke="var(--green)" stroke-width="1.3"/><line x1="5" y1="9.3" x2="7" y2="9.3" stroke="var(--green)" stroke-width="1.1"/></svg>
          347-628-9043
        </p>
        <p class="contact__line">
          <svg class="contact__icon" viewBox="0 0 12 12" aria-hidden="true"><rect x="0.5" y="2.5" width="11" height="7.5" fill="var(--green)"/><path d="M0.8,2.8 L6,7 L11.2,2.8" fill="none" stroke="var(--white)" stroke-width="1"/></svg>
          sales@brightwellholdingsllc.example
        </p>
      </div>
    </section>
  </main>
</body>
</html>
```